Family Values Poster

Need a poster for my kids (ages 5-8) that says:
Be Smart
Be Kind
Be Curious
Be Grateful
We Love You

fun, but hopefully something that they will keep for a long time

Target Market(s)

my kids

Requirements
Must have
• vertical
Nice to have
• fun and attention grabbing
Should not have
• look cheesy - not a generic inspirational poster

```html
<!DOCTYPE html>
<html lang="en">
<head>
<meta charset="utf-8">
<title>Family Values Poster</title>
<link rel="stylesheet" href="https://fonts.googleapis.com/css2?family=Nunito:wght@800;900&family=Lobster&display=swap">
<style>
  :root {
    --page: #f1f0ee;
    --brick-dark: #3f1c0c;
    --brick-mid: #5e2b14;
    --brick-lit: #a55a31;
    --lamp: #4a2512;
    --lamp-edge: #2e160a;
    --lamp-glow: #ffe7c4;
    --pup-cream: #e9d3bd;
    --pup-plum: #5c2a4a;
    --text-light: #ffffff;
    --text-shade: #bdbdbd;
    --text-drop: rgba(30, 10, 2, 0.85);
    --love-top: #f7d23a;
    --love-bottom: #d9661a;
    --love-edge: #2a1206;
  }
  * { box-sizing: border-box; margin: 0; padding: 0; }
  html, body {
    width: 1200px; height: 1200px; overflow: hidden;
    background: var(--page);
  }
  .poster {
    position: absolute; left: 210px; top: 32px;
    width: 780px; height: 1136px; overflow: hidden;
  }
  .wall {
    position: absolute; inset: 0;
    background:
      radial-gradient(ellipse 300px 330px at 394px 220px, rgba(196,112,62,0.85), rgba(140,70,35,0.35) 55%, transparent 80%),
      linear-gradient(180deg, var(--brick-mid), var(--brick-dark) 45%, var(--brick-mid) 100%);
  }
  .lamp {
    position: absolute; left: 302px; top: 14px; width: 183px; height: 95px;
  }
  .pup-art {
    position: absolute; left: 267px; top: 165px; width: 257px; height: 341px;
    border-radius: 46% 46% 40% 40%;
    background: radial-gradient(ellipse at 50% 45%, var(--pup-cream) 0%, #c9a78f 45%, var(--pup-plum) 100%);
    opacity: 0.9;
  }
  .values {
    position: absolute; left: 65px; top: 530px;
    list-style: none;
  }
  .value {
    display: flex; align-items: center; height: 102px;
  }
  .tick { width: 70px; height: 70px; flex: none; margin-right: 34px;
    filter: drop-shadow(3px 4px 2px var(--text-drop)); }
  .value-word {
    font-family: "Nunito", sans-serif; font-weight: 900;
    font-size: 94px; line-height: 1; letter-spacing: -1px;
    background: linear-gradient(180deg, var(--text-light) 30%, var(--text-shade) 100%);
    -webkit-background-clip: text; background-clip: text; color: transparent;
    filter: drop-shadow(4px 5px 2px var(--text-drop));
  }
  .sign-off {
    position: absolute; left: 0; right: 0; top: 955px;
    text-align: center;
    font-family: "Lobster", cursive; font-size: 104px; line-height: 1.1;
    background: linear-gradient(180deg, var(--love-top) 25%, var(--love-bottom) 80%);
    -webkit-background-clip: text; background-clip: text; color: transparent;
    -webkit-text-stroke: 1.5px #fff3c8;
    filter: drop-shadow(3px 4px 0 var(--love-edge));
  }
</style>
</head>
<body>
  <main class="poster">
    <div class="wall" role="img" aria-label="Brown brick wall lit by a warm spotlight"></div>
    <svg class="lamp" viewBox="0 0 183 95" role="img" aria-label="Wall lamp">
      <polygon points="14,0 169,0 183,80 0,80" fill="var(--lamp)"/>
      <rect x="0" y="78" width="183" height="10" fill="var(--lamp-edge)"/>
      <rect x="30" y="80" width="123" height="6" rx="3" fill="var(--lamp-glow)"/>
    </svg>
    <div class="pup-art" role="img" aria-label="Cartoon puppy hugging a big bone under the spotlight"></div>
    <ul class="values">
      <li class="value">
        <svg class="tick" viewBox="0 0 70 70" aria-hidden="true"><path d="M58 20 A30 30 0 1 0 64 35" fill="none" stroke="#fff" stroke-width="6" stroke-linecap="round"/><path d="M21 35 L32 46 L55 18" fill="none" stroke="#fff" stroke-width="6" stroke-linecap="round" stroke-linejoin="round"/></svg>
        <span class="value-word">Be Smart</span>
      </li>
      <li class="value">
        <svg class="tick" viewBox="0 0 70 70" aria-hidden="true"><path d="M58 20 A30 30 0 1 0 64 35" fill="none" stroke="#fff" stroke-width="6" stroke-linecap="round"/><path d="M21 35 L32 46 L55 18" fill="none" stroke="#fff" stroke-width="6" stroke-linecap="round" stroke-linejoin="round"/></svg>
        <span class="value-word">Be Kind</span>
      </li>
      <li class="value">
        <svg class="tick" viewBox="0 0 70 70" aria-hidden="true"><path d="M58 20 A30 30 0 1 0 64 35" fill="none" stroke="#fff" stroke-width="6" stroke-linecap="round"/><path d="M21 35 L32 46 L55 18" fill="none" stroke="#fff" stroke-width="6" stroke-linecap="round" stroke-linejoin="round"/></svg>
        <span class="value-word">Be Curious</span>
      </li>
      <li class="value">
        <svg class="tick" viewBox="0 0 70 70" aria-hidden="true"><path d="M58 20 A30 30 0 1 0 64 35" fill="none" stroke="#fff" stroke-width="6" stroke-linecap="round"/><path d="M21 35 L32 46 L55 18" fill="none" stroke="#fff" stroke-width="6" stroke-linecap="round" stroke-linejoin="round"/></svg>
        <span class="value-word">Be Grateful</span>
      </li>
    </ul>
    <p class="sign-off">We Love You</p>
  </main>
</body>
</html>
```